Small Catering Menu

I am looking to make a small menu for catering for my company. I am thinking of a small A5 size booklet which will also have some pictures and the cover needs to be attractive.
Likely to be 8-12 pages depending upon your design (could be less or more). I need 2-3 pages as proposal concept (Cover, inside first page and one menu page) and if we like it we will make the project guaranteed before finishing the rest of the project to add security for the designer.
Pictures will be provided to the designer whose concept is the best as they are too heavy. But use generic photos for now (rather large ones) if possible.
Logo is available and so is the inside text as well as some other tidbits.
I will provide the fonts too to ensure it maintains the corporate integrity that we are following.
Catering

```html
<!DOCTYPE html>
<html lang="en">
<head>
<meta charset="utf-8">
<title>Saffron Table Catering — The Menu</title>
<link rel="stylesheet" href="https://fonts.googleapis.com/css2?family=Montserrat:wght@700&family=Great+Vibes&display=swap">
<style>
  :root {
    --paper: #f1efea;
    --paper-shade: #e9e6df;
    --saffron: #dda54f;
    --ink: #1b1b1b;
  }
  html, body {
    margin: 0;
    padding: 0;
    width: 856px;
    height: 1200px;
    overflow: hidden;
    background: var(--paper);
  }
  .menu-cover {
    position: relative;
    width: 856px;
    height: 1200px;
    background: radial-gradient(ellipse at 55% 45%, var(--paper) 0%, var(--paper) 55%, var(--paper-shade) 100%);
    overflow: hidden;
  }
  .spine-band {
    position: absolute;
    left: 0;
    top: 0;
    width: 42px;
    height: 100%;
    background: var(--saffron);
  }
  .brand {
    position: absolute;
    left: 446px;
    top: 594px;
    transform: translate(-50%, -50%);
    display: flex;
    align-items: center;
    gap: 22px;
    white-space: nowrap;
  }
  .brand-mark {
    width: 96px;
    height: 96px;
    background: var(--saffron);
    flex: none;
  }
  .brand-name {
    font-family: "Montserrat", Arial, sans-serif;
    font-weight: 700;
    font-size: 46px;
    line-height: 1.12;
    letter-spacing: 1px;
    text-transform: uppercase;
    color: var(--ink);
  }
  .brand-name span {
    display: block;
  }
  .cover-title {
    position: absolute;
    right: 36px;
    bottom: 30px;
    margin: 0;
    font-family: "Great Vibes", cursive;
    font-weight: 400;
    color: var(--ink);
    line-height: 1;
    text-align: right;
  }
  .cover-title .article {
    display: block;
    font-size: 50px;
    margin-right: 150px;
    margin-bottom: -6px;
  }
  .cover-title .word {
    display: block;
    font-size: 112px;
  }
</style>
</head>
<body>
  <main class="menu-cover">
    <div class="spine-band"></div>
    <div class="brand">
      <span class="brand-mark"></span>
      <span class="brand-name">
        <span>Saffron Table</span>
        <span>Catering</span>
      </span>
    </div>
    <h1 class="cover-title">
      <span class="article">the</span>
      <span class="word">Menu</span>
    </h1>
  </main>
</body>
</html>
```